TRU PEAK POWER.

I'd like my business logo.
contact name: Desmond Halvik
phone:0438275160
email: info@trupeakpower.net.au
website: www.trupeakpower.net.au

services:
solar
battery storage
LED lighting
energy saving solutions
general electrical
I'd like the design to look professional

Target Market(s)

Everyone

Industry/Entity Type

Business

Contact Information for Business Card

as described above

Requirements
Must have
• Id like the colours and the design to work well with my logo.

```html
<!DOCTYPE html>
<html lang="en">
<head>
<meta charset="utf-8">
<title>Tru Peak Power – Business Card</title>
<link rel="stylesheet" href="https://fonts.googleapis.com/css2?family=Noto+Sans:wght@400;700&display=swap">
<style>
  :root {
    --frame-top: #52b07a;
    --frame-bottom: #8cc13c;
    --panel-top: #ffffff;
    --panel-mid: #e4efc6;
    --panel-bottom: #a9d055;
    --brand-green: #3f9a3a;
    --sun-orange: #f5a524;
    --accent-light: #9ccb45;
    --accent-dark: #7ab836;
    --ink: #111111;
  }
  html, body {
    margin: 0;
    padding: 0;
    width: 1200px;
    height: 683px;
    overflow: hidden;
    background: #ffffff;
  }
  .card {
    position: relative;
    width: 1200px;
    height: 683px;
    background: linear-gradient(180deg, var(--frame-top) 0%, var(--frame-bottom) 100%);
    font-family: "Noto Sans", sans-serif;
    color: var(--ink);
    overflow: hidden;
  }
  .card__panel {
    position: absolute;
    left: 14px;
    top: 14px;
    right: 12px;
    bottom: 14px;
    background: linear-gradient(180deg, var(--panel-top) 0%, var(--panel-mid) 45%, var(--panel-bottom) 100%);
  }
  .card__accent {
    position: absolute;
    left: 990px;
    top: 300px;
    width: 198px;
    height: 369px;
    border-top-left-radius: 100% 100%;
    background: linear-gradient(180deg, var(--accent-light) 0%, var(--accent-dark) 100%);
  }
  .brand {
    position: absolute;
    left: 150px;
    top: 170px;
    display: flex;
    align-items: center;
    gap: 34px;
  }
  .brand__mark {
    width: 120px;
    height: 120px;
    border-radius: 50%;
    background: var(--sun-orange);
  }
  .brand__name {
    margin: 0;
    font-size: 92px;
    font-weight: 700;
    line-height: 1;
    color: var(--brand-green);
    letter-spacing: 1px;
    white-space: nowrap;
  }
  .contact {
    position: absolute;
    left: 44px;
    top: 444px;
    margin: 0;
    display: grid;
    grid-template-columns: 288px auto;
    font-size: 30px;
    line-height: 35px;
    letter-spacing: 0.8px;
  }
  .contact dt, .contact dd { margin: 0; white-space: nowrap; }
  .services {
    position: absolute;
    left: 42px;
    top: 632px;
    margin: 0;
    padding: 0;
    list-style: none;
    display: flex;
    gap: 22px;
    font-size: 23px;
    line-height: 30px;
    white-space: nowrap;
  }
</style>
</head>
<body>
<main class="card">
  <div class="card__panel"></div>
  <div class="card__accent" role="img" aria-label="Decorative green leaf swoosh in the lower right corner"></div>

  <header class="brand">
    <span class="brand__mark" aria-hidden="true"></span>
    <h1 class="brand__name">Tru Peak Power</h1>
  </header>

  <dl class="contact">
    <dt>Contact name:</dt><dd>Desmond Halvik</dd>
    <dt>Tel:</dt><dd>0438275160</dd>
    <dt>Email:</dt><dd>info@trupeakpower.net.au</dd>
    <dt>Website:</dt><dd>www.trupeakpower.net.au</dd>
  </dl>

  <ul class="services">
    <li>Energy saving solutions</li>
    <li>LED lighting</li>
    <li>Battery storage</li>
    <li>Solar</li>
    <li>General electrical</li>
  </ul>
</main>
</body>
</html>
```